BRISKFIELD METRO ATHLETIDOME INVESTMENT BROCHURE*

We need an investment brochure for a new sportsplex being built to service the Greater Toronto Area. The attached file called "Brochure 2020" can be repurposed, with the Briskfield Metro Athletidome name and logo inserted wherever the Loftway Pitch Yard info currently exists.

We have also provided an excel file with 3 sheets-- each of these sheets is to be inserted into the brochure.

Target Market(s)

Investors

Logo Text

BRISKFIELD ATHLETIDOME

Requirements
Must have
• Project must reference:
The Worldwide trend to small sided soccer.

Investment opportunity that is eligible for registered funds (RRSPs and TFSAs)

Briskfield Metro Athletidome is a unique combination of sport and court that allows both players and spectators to be immersed with a fast-paced, high-energy game.
Should not have
• No wording or pages that reference "American" or USA.

```html
<!DOCTYPE html>
<html lang="en">
<head>
<meta charset="utf-8">
<title>Revenue Projections – Twin Pad Indoor Soccer Park</title>
<link href="https://fonts.googleapis.com/css2?family=Montserrat:ital,wght@0,400;0,500;0,700;1,400&family=Poppins:wght@800&display=swap" rel="stylesheet">
<style>
  :root {
    --gold-1: #c9a64a;
    --gold-2: #9a8446;
    --gold-3: #6b6a4a;
    --ink: #222;
    --rule: #3a3a3a;
    --header-pink: #f5c7d8;
    --cons-band: #f2b98e;
    --cons-text: #e0782c;
    --cons-row: rgba(250, 240, 232, 0.92);
    --target-band: #92d38c;
    --target-text: #3fae48;
    --target-row: rgba(214, 236, 206, 0.9);
    --goal-row: #f2ef8c;
    --out-band: #7ccbe8;
    --out-text: #1f92c9;
    --out-row: rgba(214, 232, 240, 0.9);
    --white: #fff;
  }
  * { box-sizing: border-box; margin: 0; padding: 0; }
  html, body { width: 1200px; height: 729px; overflow: hidden; }
  body { font-family: "Montserrat", sans-serif; color: var(--ink); }
  .canvas {
    position: relative; width: 1200px; height: 729px; overflow: hidden;
  }
  .venue-backdrop {
    position: absolute; inset: 0;
    background:
      linear-gradient(180deg, rgba(0,0,0,0) 70%, rgba(40,60,30,0.55) 100%),
      radial-gradient(ellipse at 30% 20%, #d9b756 0%, var(--gold-1) 35%, var(--gold-2) 70%, var(--gold-3) 100%);
  }
  .venue-photo {
    position: absolute; left: 893px; top: 0; width: 307px; height: 334px;
    background: linear-gradient(160deg, #b9a98a 0%, #8a8a72 40%, #4e6a3c 75%, #3d5530 100%);
  }
  .title {
    position: absolute; left: 44px; top: 30px; width: 821px;
    text-align: center; font-family: "Poppins", sans-serif; font-weight: 800;
    font-size: 33px; line-height: 40px; color: var(--white);
    text-shadow: 2px 2px 0 #2a2a2a, 3px 3px 4px rgba(0,0,0,0.5);
  }
  .projections {
    position: absolute; left: 44px; top: 122px; width: 821px;
    border-collapse: collapse; table-layout: fixed; font-size: 10.5px;
  }
  .projections th, .projections td {
    border: 1px solid var(--rule); text-align: center; vertical-align: middle;
    line-height: 12px;
  }
  .projections th {
    background: var(--header-pink); font-weight: 400; height: 43px; font-size: 9.6px; line-height: 11px;
  }
  .projections td.scenario { text-align: left; padding-left: 4px; font-size: 10px; line-height: 12px; }
  .projections tr.two-line td { height: 33px; }
  .projections tr.one-line td { height: 19.5px; }
  .projections tr.section td {
    height: 20px; text-align: left; padding-left: 4px; font-weight: 700; font-size: 11px;
  }
  .projections td.roi { font-weight: 700; }
  .conservative td { background: var(--cons-row); }
  .conservative.section td { background: var(--cons-band); color: var(--cons-text); }
  .target td { background: var(--target-row); }
  .target.section td { background: var(--target-band); color: var(--target-text); }
  .target.goal td { background: var(--goal-row); color: var(--target-text); }
  .target.goal td.roi { font-size: 14px; }
  .outperform td { background: var(--out-row); }
  .outperform.section td { background: var(--out-band); color: var(--out-text); }
  .definitions {
    position: absolute; left: 893px; top: 350px; width: 264px; height: 210px;
    background: var(--white); padding: 6px 7px; font-size: 10px; line-height: 12px;
  }
  .definitions h2 { font-size: 10.5px; font-weight: 700; text-align: center; margin-bottom: 4px; }
  .definitions dl { display: grid; grid-template-columns: 122px 1fr; row-gap: 5px; }
  .definitions dt { font-weight: 700; }
  .definitions dd { font-style: italic; }
</style>
</head>
<body>
<div class="canvas">
  <div class="venue-backdrop" role="img" aria-label="Rendered interior of an indoor soccer park with players on artificial turf and spectators on benches"></div>
  <div class="venue-photo" role="img" aria-label="Rendered view of a youth match on a covered turf pad with spectators watching"></div>

  <h1 class="title">Revenue Projections for a Twin Pad Indoor<br>Soccer Park Centrally located in the GTA</h1>

  <table class="projections">
    <colgroup>
      <col style="width:173px"><col style="width:69px"><col style="width:69px"><col style="width:70px">
      <col style="width:69px"><col style="width:69px"><col style="width:69px"><col style="width:69px">
      <col style="width:69px"><col style="width:51px"><col style="width:44px">
    </colgroup>
    <thead>
      <tr>
        <th>Scenario</th><th>Avg Hourly Rate</th><th>Weekly</th><th>Monthly</th><th>Annually</th>
        <th>Total Expenses</th><th>Net Income</th><th>50% Investors</th><th>50% Management Group</th>
        <th>Investor ROI</th><th>Total ROI</th>
      </tr>
    </thead>
    <tbody>
      <tr class="conservative section"><td colspan="11">CONSERVATIVE</td></tr>
      <tr class="conservative two-line"><td class="scenario">Baseline (6 months full capacity, 6 months 25% capacity)</td><td>$140</td><td>$7,700</td><td>$33,367</td><td>$400,400</td><td>$351,700</td><td>$48,700</td><td>$24,350</td><td>$24,350</td><td class="roi">5%</td><td class="roi">10%</td></tr>
      <tr class="conservative two-line"><td class="scenario">Goal (8 months full capacity, 4 months 40% capacity)</td><td>$140</td><td>$9,283</td><td>$40,227</td><td>$482,720</td><td>$369,285</td><td>$113,435</td><td>$56,718</td><td>$56,718</td><td class="roi">11%</td><td class="roi">22%</td></tr>
      <tr class="conservative two-line"><td class="scenario">Stretch 10 months full capacity, 2 months 40% capacity)</td><td>$140</td><td>$11,041</td><td>$47,843</td><td>$574,112</td><td>$387,749</td><td>$186,363</td><td>$93,181</td><td>$93,181</td><td class="roi">18%</td><td class="roi">36%</td></tr>
      <tr class="conservative one-line"><td class="scenario">Full Capacity</td><td>$140</td><td>$12,320</td><td>$53,387</td><td>$640,640</td><td>$407,137</td><td>$233,503</td><td>$116,752</td><td>$116,752</td><td class="roi">22%</td><td class="roi">45%</td></tr>

      <tr class="target section"><td colspan="11">TARGET</td></tr>
      <tr class="target two-line"><td class="scenario">Baseline (6 months full capacity, 6 months 25% capacity)</td><td>$155</td><td>$8,525</td><td>$36,942</td><td>$443,300</td><td>$351,700</td><td>$91,600</td><td>$45,800</td><td>$45,800</td><td class="roi">9%</td><td class="roi">18%</td></tr>
      <tr class="target goal two-line"><td class="scenario">Goal (8 months full capacity, 4 months 40% capacity)</td><td>$155</td><td>$10,036</td><td>$43,489</td><td>$521,864</td><td>$369,285</td><td>$152,579</td><td>$76,290</td><td>$76,290</td><td class="roi">15%</td><td class="roi">30%</td></tr>
      <tr class="target two-line"><td class="scenario">Stretch 10 months full capacity, 2 months 40% capacity)</td><td>$155</td><td>$12,224</td><td>$52,969</td><td>$635,624</td><td>$387,749</td><td>$247,875</td><td>$123,937</td><td>$123,937</td><td class="roi">24%</td><td class="roi">48%</td></tr>
      <tr class="target one-line"><td class="scenario">Full Capacity</td><td></td><td>$13,640</td><td>$59,107</td><td>$709,280</td><td>$407,137</td><td>$302,143</td><td>$151,072</td><td>$151,072</td><td class="roi">29%</td><td class="roi">58%</td></tr>

      <tr class="outperform section"><td colspan="11">OUTPERFORM</td></tr>
      <tr class="outperform two-line"><td class="scenario">Baseline (6 months full capacity, 6 months 25% capacity)</td><td>$170</td><td>$9,350</td><td>$40,517</td><td>$486,200</td><td>$351,700</td><td>$134,500</td><td>$67,250</td><td>$67,250</td><td class="roi">13%</td><td class="roi">26%</td></tr>
      <tr class="outperform two-line"><td class="scenario">Goal (8 months full capacity, 4 months 40% capacity)</td><td>$170</td><td>$10,807</td><td>$46,831</td><td>$561,968</td><td>$369,285</td><td>$192,683</td><td>$96,342</td><td>$96,342</td><td class="roi">19%</td><td class="roi">38%</td></tr>
      <tr class="outperform two-line"><td class="scenario">Stretch 10 months full capacity, 2 months 40% capacity)</td><td>$170</td><td>$13,406</td><td>$58,095</td><td>$697,136</td><td>$387,749</td><td>$309,387</td><td>$154,693</td><td>$154,693</td><td class="roi">30%</td><td class="roi">60%</td></tr>
      <tr class="outperform one-line"><td class="scenario">Full Capacity</td><td>$170</td><td>$14,960</td><td>$64,827</td><td>$777,920</td><td>$407,137</td><td>$370,783</td><td>$185,392</td><td>$185,392</td><td class="roi">36%</td><td class="roi">72%</td></tr>
    </tbody>
  </table>

  <section class="definitions">
    <h2>DEFINITIONS:</h2>
    <dl>
      <dt>Full Capacity</dt><dd>Weekends and Holidays fully booked 8am to 10pm Weekdays fully booked 4pm to 10pm</dd>
      <dt>6 months full capacity</dt><dd>November 1st to April 30th</dd>
      <dt>8 months full capacity</dt><dd>September 1st to April 30th</dd>
      <dt>10 months full capacity</dt><dd>September 1st to June 30th</dd>
      <dt>Avg Hourly Rate</dt><dd>Rental Rate per hour, per pad.</dd>
      <dt>Investor ROI</dt><dd></dd>
    </dl>
  </section>
</div>
</body>
</html>
```